Brightpagekit.com Website Design

We would like to redesign brightpagkit.com and we are looking for creative ideas. The new design should be clean and not resemble with any other existing website design.

The most important factor is that website have many banners/advertisements so the new design should be able to accommodate these banners of different size (Advertisement Friendly Design)

All Tools should be categorized under different main categories like all those tools that are related to content/writing will be shown under Content Tools ( Please find all categories and tools in attached file with the project). Right now all tools are showing randomly.

Also, Design single tool pages with sidebar, advertisement, and content placement.
ex. brightpagekit.com/plagiarism-checker/
brightpagekit.com/keyword-position/

Winning designer will also make the logo as well.

Target Market(s)

SEO Agencies, SEO executive, Article writers, Essay Writers, Plagiarism Checkers, Webmasters

Industry/Entity Type

Seo

Logo Text

Bright Page Kit

Number of Pages Required

5+ page

Font styles to use
Serif
Sans Serif
Other font styles liked:
• Any

Colors

Designer to choose colors to be used in the design.

Requirements
Must have
• 1) Clean Design
• 2) Modern Look
• 3) Easy To Navigate
• 4) Separate Icon for every Tool
• 5) Advertisement/Banners Freindly Design
Nice to have
• Matching Logo
• WOW Factor
Should not have
• Complex Design
• No drop down menu

```html
<!DOCTYPE html>
<html lang="en">
<head>
<meta charset="utf-8">
<title>Bright Page Kit – Free Online SEO Tools</title>
<link href="https://fonts.googleapis.com/css2?family=Roboto:wght@400;500;700;900&display=swap" rel="stylesheet">
<style>
:root{
  --green:#137a47;
  --green-dark:#0e6339;
  --red:#e9524f;
  --navy:#1b2e45;
  --ink:#2a2a2a;
  --muted:#555;
  --line:#d7d7d7;
  --footer:#1f2b38;
  --teal:#1d8f95;
  --yellow:#f6c21c;
  --blue:#1b4fb0;
}
*{box-sizing:border-box;margin:0;padding:0}
html,body{width:1200px;height:2423px;overflow:hidden}
body{position:relative;background:#fff;font-family:'Roboto',Arial,sans-serif;color:var(--ink)}

/* header */
.site-header{position:absolute;left:0;top:0;width:1200px;height:76px;background:#fff}
.brand{position:absolute;left:153px;top:18px;display:flex;align-items:center;gap:10px}
.brand-dot{width:34px;height:34px;border-radius:50%;background:var(--green)}
.brand-name{font-size:30px;font-weight:700;color:var(--navy);letter-spacing:-.5px}
.main-nav{position:absolute;left:436px;top:29px;display:flex;gap:0}
.main-nav a{font-size:12.5px;color:#222;text-decoration:none;text-transform:uppercase;margin-right:26px}
.btn{position:absolute;top:23px;height:30px;border-radius:3px;color:#fff;font-size:12.5px;display:flex;align-items:center;justify-content:center;text-transform:uppercase}
.btn-login{left:882px;width:79px;background:var(--green)}
.btn-register{left:969px;width:81px;background:var(--red)}

/* hero */
.hero{position:absolute;left:0;top:76px;width:1200px;height:336px;
  background:linear-gradient(100deg,#6d88a6 0%,#c9d6e2 22%,#eef0ee 45%,#d9d2c4 62%,#c0494a 82%,#9d2a2c 100%)}
.search-box{position:absolute;left:250px;top:145px;width:695px;height:70px;background:rgba(255,255,255,.55);border-radius:6px}
.search-input{position:absolute;left:12px;top:12px;width:508px;height:48px;background:#fff;border-radius:4px;font-size:13px;color:#777;padding:17px 14px}
.search-btn{position:absolute;left:532px;top:10px;width:155px;height:50px;background:var(--green);color:#fff;border-radius:4px;font-size:16px;font-weight:500;display:flex;align-items:center;justify-content:center}

/* categories */
.category{position:absolute;left:150px;width:641px}
.category-head{position:relative;height:44px;border-bottom:4px solid var(--green)}
.category-title{font-size:32px;font-weight:500;color:var(--green);line-height:36px}
.category-head::after{content:"";position:absolute;right:4px;bottom:10px;border:7px solid transparent;border-top:8px solid var(--green);border-bottom:0}
.tool-grid{margin-top:21px;display:grid;grid-template-columns:repeat(4,150px);column-gap:13.6px;row-gap:28px}
.tool{height:125px;border:1px solid var(--line);box-shadow:0 1px 3px rgba(0,0,0,.12);background:#fff;display:flex;flex-direction:column}
.tool-icon{flex:1;display:flex;align-items:center;justify-content:center}
.tool-icon svg{width:62px;height:62px;fill:none;stroke:var(--navy);stroke-width:3.2;stroke-linecap:round;stroke-linejoin:round}
.tool-icon svg .f{fill:var(--navy);stroke:none}
.tool-label{height:37px;background:var(--green);color:#fff;font-size:11.5px;line-height:14px;text-align:center;display:flex;align-items:center;justify-content:center;padding:0 6px}

.view-more{position:absolute;left:150px;top:2145px;width:158px;height:40px;background:var(--red);color:#fff;font-size:15px;font-weight:500;border-radius:2px;display:flex;align-items:center;justify-content:center}

/* sidebar */
.sidebar{position:absolute;left:824px;top:447px;width:226px}
.ad{position:relative;width:226px;overflow:hidden;color:#fff}
.ad-plag{height:113px;background:linear-gradient(135deg,#2aa3a8,#146f78)}
.ad-plag .tag{position:absolute;right:0;top:0;background:#0c5b61;font-size:12px;padding:4px 10px}
.ad-plag .kicker{position:absolute;left:12px;top:6px;font-size:17px;font-weight:500}
.ad-plag .title{position:absolute;left:12px;top:25px;font-size:27px;font-weight:700;line-height:27px}
.ad-plag .sub{position:absolute;left:18px;top:90px;font-size:11px}
.ad-plag .corner{position:absolute;right:-6px;bottom:12px;transform:rotate(-40deg);font-size:12px;font-weight:700}
.ad-da70{height:113px;margin-top:5px;background:linear-gradient(110deg,#3e1a1a 0%,#8f2424 40%,#e0433a 100%)}
.ad-da70 .big{position:absolute;right:14px;top:12px;font-size:36px;font-weight:900;line-height:36px}
.ad-da70 .mid{position:absolute;right:14px;top:48px;font-size:23px;font-weight:700}
.ad-da70 .pill{position:absolute;right:12px;top:82px;background:#2d9bd8;border-radius:4px;padding:3px 14px;font-size:17px;font-weight:700}
.popular{margin-top:13px;border:1px solid var(--line)}
.popular-head{height:39px;display:flex;align-items:center;justify-content:center;font-size:17px;font-weight:700;color:var(--green);text-transform:uppercase;border-bottom:2px solid var(--green)}
.popular-list{list-style:none}
.popular-list li{height:32px;border-bottom:1px solid #e6e6e6;font-size:11px;color:#444;padding:10px 0 0 20px}
.popular-list li.active{background:var(--green);color:#fff}
.rank-box{margin-top:10px;height:113px;background:#efefef;text-align:center;position:relative}
.rank-box .line1{padding-top:14px;font-size:15px;font-weight:700;color:#e02a2a}
.rank-box .line2{font-size:13px;font-weight:500;color:#222}
.rank-bar{position:absolute;left:0;bottom:0;width:226px;height:52px;background:#3a3a3a}
.rank-input{position:absolute;left:8px;top:14px;width:150px;height:22px;background:#fff;font-size:11px;color:#555;padding:4px 6px;text-align:left}
.rank-btn{position:absolute;left:166px;top:14px;width:50px;height:22px;background:#fff;color:var(--green);font-size:12px;font-weight:700;text-decoration:underline;padding-top:3px}
.ad-da80{margin-top:10px;height:113px;background:var(--yellow);color:#111}
.ad-da80 .big{position:absolute;left:0;width:226px;top:4px;text-align:center;font-size:62px;font-weight:900;line-height:64px}
.ad-da80 .bar{position:absolute;left:30px;top:70px;width:166px;height:10px;background:linear-gradient(90deg,#3aa335,#a6d44b)}
.ad-da80 .buy{position:absolute;left:12px;top:84px;font-size:20px;font-weight:900;color:#c62020}
.ad-da80 .buy span{font-size:15px;color:#111}
.ad-boost{margin-top:8px;height:113px;background:linear-gradient(135deg,#0d2d78,#1b4fb0 60%,#0b1f56)}
.ad-boost .person{position:absolute;left:62px;top:14px;width:46px;height:99px;background:#3a5fa8;border-radius:23px 23px 0 0}
.ad-boost .h1{position:absolute;right:8px;top:6px;font-size:14px;font-weight:700;color:#fff}
.ad-boost .h2{position:absolute;right:8px;top:22px;font-size:24px;font-weight:900;color:#fff}
.ad-boost .h3{position:absolute;right:14px;top:52px;font-size:12px;font-weight:700;color:#ffd23a}
.ad-boost .side{position:absolute;left:6px;top:60px;font-size:8px;line-height:10px;font-weight:700}
.ad-boost .price{position:absolute;right:6px;bottom:6px;background:#e23b2e;border-radius:3px;padding:2px 6px;font-size:10px;line-height:11px;text-align:center}
.ad-boost .price b{font-size:15px;display:block;line-height:16px}

/* footer */
.site-footer{position:absolute;left:0;top:2253px;width:1200px;height:170px;background:var(--footer);color:#fff}
.footer-about{position:absolute;left:174px;top:32px;width:470px}
.footer-head{font-size:11px;font-weight:700;letter-spacing:1px;text-transform:uppercase;margin-bottom:14px}
.footer-about p{font-size:10.5px;line-height:15px}
.footer-links{position:absolute;left:698px;top:32px;width:345px}
.footer-links .links{font-size:10.5px;padding-bottom:8px;border-bottom:1px solid #7a8896}
.footer-links .links span{margin:0 6px;color:#aab}
.subscribe-label{margin-top:11px;font-size:10.5px;font-weight:700}
.subscribe{margin-top:6px;display:flex;align-items:center}
.subscribe-ico{width:28px;height:28px;background:var(--green);display:flex;align-items:center;justify-content:center}
.subscribe-input{width:199px;height:28px;background:#fff;color:#888;font-size:11px;padding:8px 8px}
.subscribe-btn{margin-left:12px;width:108px;height:28px;border:1px solid var(--green);background:#0c1a14;font-size:11.5px;display:flex;align-items:center;justify-content:center}
</style>
</head>
<body>

<header class="site-header">
  <div class="brand"><span class="brand-dot"></span><span class="brand-name">Bright Page Kit</span></div>
  <nav class="main-nav"><a>Home</a><a>Plagiarism Checker</a><a>Advertise</a><a>Blog</a><a>Contact Us</a></nav>
  <a class="btn btn-login">Login</a>
  <a class="btn btn-register">Register</a>
</header>

<section class="hero" role="img" aria-label="Desk scene with notebook reading SEO, glasses and a red mug">
  <div class="search-box">
    <div class="search-input">Type any word to search from seo tool</div>
    <div class="search-btn">SEARCH</div>
  </div>
</section>

<!-- Content tools -->
<section class="category" style="top:445px">
  <div class="category-head"><h2 class="category-title">Content Tools</h2></div>
  <div class="tool-grid">
    <div class="tool"><div class="tool-icon"><svg viewBox="0 0 48 48"><path class="f" d="M14 6h12l8 8v20H14z"/><path class="f" d="M18 14v28h20V20h-2v20H20V14z" opacity=".9"/></svg></div><div class="tool-label">Plagiarism Checker</div></div>
    <div class="tool"><div class="tool-icon"><svg viewBox="0 0 48 48"><circle class="f" cx="24" cy="24" r="20"/><rect x="15" y="14" width="16" height="20" stroke="#fff" stroke-width="2"/><path d="M18 19h10M18 23h10M18 27h7M30 31l5-8" stroke="#fff" stroke-width="2"/></svg></div><div class="tool-label">Article Rewriter</div></div>
    <div class="tool"><div class="tool-icon"><svg viewBox="0 0 48 48" style="width:80px"><rect x="2" y="15" width="14" height="14" stroke-width="2.4"/><path d="M5 22l3 3 6-7" stroke-width="2.4"/><text x="19" y="30" class="f" font-family="Roboto,sans-serif" font-size="16">ABC</text></svg></div><div class="tool-label">Spell Checker</div></div>
    <div class="tool"><div class="tool-icon"><svg viewBox="0 0 48 48"><rect x="6" y="6" width="14" height="14"/><rect x="28" y="6" width="14" height="14"/><rect x="6" y="28" width="14" height="14"/><rect class="f" x="11" y="11" width="4" height="4"/><rect class="f" x="33" y="11" width="4" height="4"/><rect class="f" x="11" y="33" width="4" height="4"/><path class="f" d="M28 28h5v5h-5zM37 28h5v5h-5zM33 33h4v4h-4zM28 37h5v5h-5zM37 37h5v5h-5z"/></svg></div><div class="tool-label">Online MD5 Generator</div></div>
    <div class="tool"><div class="tool-icon"><svg viewBox="0 0 48 48"><rect class="f" x="6" y="6" width="36" height="36"/><path d="M16 36l8-24 8 24M19 28h10" stroke="#fff" stroke-width="3.4"/></svg></div><div class="tool-label">Grammar Checker</div></div>
    <div class="tool"><div class="tool-icon"><svg viewBox="0 0 48 48"><path d="M10 4h20l8 8v32H10z"/><path d="M30 4v8h8"/><path d="M16 22l3 12 5-9 5 9 3-12"/></svg></div><div class="tool-label">Word Count Checker</div></div>
    <div class="tool"><div class="tool-icon"><svg viewBox="0 0 48 48"><path d="M6 14h34M32 7l8 7-8 7M42 34H8M16 27l-8 7 8 7"/><text x="20" y="30" class="f" font-family="Roboto,sans-serif" font-size="10" font-weight="700">Tr</text></svg></div><div class="tool-label">Change Text Case</div></div>
    <div class="tool"><div class="tool-icon"><svg viewBox="0 0 48 48"><path d="M12 6h24M24 6v28M6 40h14M16 36l4 4-4 4M42 40H28M32 36l-4 4 4 4"/></svg></div><div class="tool-label">Merge Words Online Tool</div></div>
  </div>
</section>

<!-- Images -->
<section class="category" style="top:822px">
  <div class="category-head"><h2 class="category-title">Images Handling Tool</h2></div>
  <div class="tool-grid">
    <div class="tool"><div class="tool-icon"><svg viewBox="0 0 48 48"><rect x="5" y="8" width="38" height="32"/><path class="f" d="M9 36l11-13 8 9 5-5 6 9z"/><circle class="f" cx="33" cy="17" r="3.5"/></svg></div><div class="tool-label">Reverse Image Search</div></div>
    <div class="tool"><div class="tool-icon"><svg viewBox="0 0 48 48"><rect x="5" y="6" width="16" height="36" rx="3"/><path d="M5 18h16M5 30h16M26 10h16M26 18h12M26 24h16M26 30h12M26 38h16"/></svg></div><div class="tool-label">Image Compression</div></div>
    <div class="tool"><div class="tool-icon"><svg viewBox="0 0 48 48"><rect x="4" y="4" width="40" height="40" stroke-width="2"/><rect x="14" y="14" width="20" height="20" stroke-width="2.4"/><path class="f" d="M16 32l6-7 4 4 3-3 4 6z"/><path d="M4 4l8 8M44 44l-8-8" stroke-width="2"/></svg></div><div class="tool-label">Image Resizer</div></div>
    <div class="tool"><div class="tool-icon"><svg viewBox="0 0 48 48"><path d="M14 4v30h30M4 14h30v30M40 8L8 40"/></svg></div><div class="tool-label">Crop Image</div></div>
    <div class="tool"><div class="tool-icon"><svg viewBox="0 0 48 48"><rect x="5" y="8" width="38" height="32"/><path class="f" d="M9 36l11-13 8 9 5-5 6 9z"/><circle class="f" cx="33" cy="17" r="3.5"/></svg></div><div class="tool-label">Favicon Generator Tool</div></div>
    <div class="tool"><div class="tool-icon"><svg viewBox="0 0 48 48"><rect x="4" y="18" width="18" height="14" rx="2" stroke-width="2.4"/><path class="f" d="M11 22l6 3-6 3z"/><circle cx="34" cy="20" r="10" stroke-width="2.4"/><text x="27" y="23.5" class="f" font-family="Roboto,sans-serif" font-size="8" font-weight="700">GIF</text><path d="M16 40c6 2 12 0 16-8" stroke-width="2"/></svg></div><div class="tool-label">Video to GIF Converter</div></div>
    <div class="tool"><div class="tool-icon"><svg viewBox="0 0 48 48"><path class="f" d="M8 4h24l8 8v32H8z"/><path d="M22 12c6 0 9 3 9 8M27 17l4 4 4-4" stroke="#fff" stroke-width="2.4"/><rect x="8" y="28" width="32" height="12" fill="#fff" stroke="none"/><text x="14" y="38" class="f" font-family="Roboto,sans-serif" font-size="10" font-weight="700">JPG</text></svg></div><div class="tool-label">Convert to JPG</div></div>
  </div>
</section>

<!-- Keywords -->
<section class="category" style="top:1205px">
  <div class="category-head"><h2 class="category-title">Keywords Tools</h2></div>
  <div class="tool-grid">
    <div class="tool"><div class="tool-icon"><svg viewBox="0 0 48 48"><path d="M5 6v36h38M10 34l10-12 7 6 12-14M32 14h7v7"/></svg></div><div class="tool-label">Keyword Position</div></div>
    <div class="tool"><div class="tool-icon"><svg viewBox="0 0 48 48"><path d="M10 4h20l8 8v32H10z"/><path d="M30 4v8h8M15 14h10M15 20h6"/><circle cx="25" cy="29" r="7"/><path d="M22 29h6M30 34l5 5"/></svg></div><div class="tool-label">Keywords Density Checker</div></div>
    <div class="tool"><div class="tool-icon"><svg viewBox="0 0 48 48"><circle class="f" cx="24" cy="24" r="20"/><path d="M18 19c0-4 3-6 6-6s6 2 6 6c0 5-6 5-6 10" stroke="#fff" stroke-width="3.6"/><circle cx="24" cy="35" r="2.2" fill="#fff" stroke="none"/></svg></div><div class="tool-label">Keywords Suggestions Tool</div></div>
    <div class="tool"><div class="tool-icon"><svg viewBox="0 0 48 48"><path class="f" d="M4 8h7v6H4zM15 8h29v6H15zM4 19h7v6H4zM15 19h29v6H15zM4 30h7v6H4zM15 30h29v6H15zM4 41h7v3H4zM15 41h29v3H15z"/></svg></div><div class="tool-label">Website Keywords Suggestions Tool</div></div>
    <div class="tool"><div class="tool-icon"><svg viewBox="0 0 48 48"><path d="M24 8H8v32h32V24"/><path d="M38 6l4 4-16 16-6 2 2-6z"/></svg></div><div class="tool-label">keywords Rich Domains Suggestions Tool</div></div>
    <div class="tool"><div class="tool-icon"><svg viewBox="0 0 48 48" style="width:70px"><rect x="3" y="12" width="42" height="24" rx="2" stroke-width="2.4"/><path d="M8 18h4M15 18h4M22 18h4M29 18h4M36 18h4M8 24h4M15 24h4M22 24h4M29 24h4M36 24h4M12 30h24" stroke-width="2.2"/></svg></div><div class="tool-label">Related keywords Finder</div></div>
    <div class="tool"><div class="tool-icon"><svg viewBox="0 0 48 48"><path d="M6 4v40h38M6 8c14 0 14 32 34 32M22 26l16-16M30 10h8v8"/></svg></div><div class="tool-label">Long Tail Keyword Suggestion Tool</div></div>
    <div class="tool"><div class="tool-icon"><svg viewBox="0 0 48 48"><path d="M8 6h32v26l-16 12L8 32z"/><path d="M8 12h32" stroke-width="2"/><circle class="f" cx="24" cy="26" r="7"/><text x="21" y="29" fill="#fff" font-family="Roboto,sans-serif" font-size="8" font-weight="700">B</text></svg></div><div class="tool-label">Keyword Competition Checker</div></div>
    <div class="tool"><div class="tool-icon"><svg viewBox="0 0 48 48"><path class="f" d="M6 20h9v24H6zM19 10h9v34h-9zM32 16h9v28h-9zM2 44h44v2H2z"/><path d="M10.5 13l1 2h2l-1.6 1.2.6 2-2-1.2-2 1.2.6-2L7.5 15h2zM23.5 3l1 2h2l-1.6 1.2.6 2-2-1.2-2 1.2.6-2L20.5 5h2zM36.5 9l1 2h2l-1.6 1.2.6 2-2-1.2-2 1.2.6-2L33.5 11h2z" stroke-width="1.2"/></svg></div><div class="tool-label">SEO Keyword Competition Analysis</div></div>
  </div>
</section>

<!-- Backlinks -->
<section class="category" style="top:1742px">
  <div class="category-head"><h2 class="category-title">BackLink Tools</h2></div>
  <div class="tool-grid">
    <div class="tool"><div class="tool-icon"><svg viewBox="0 0 48 48" style="stroke-width:5"><path d="M22 14l6-6a8 8 0 0112 12l-6 6M26 34l-6 6A8 8 0 018 28l6-6M18 30l12-12"/></svg></div><div class="tool-label">Backlink Checker</div></div>
    <div class="tool"><div class="tool-icon"><svg viewBox="0 0 48 48" style="stroke-width:4"><rect x="14" y="2" width="12" height="18" rx="6" transform="rotate(-30 20 11)"/><rect x="22" y="14" width="12" height="18" rx="6" transform="rotate(-30 28 23)"/><rect x="14" y="28" width="12" height="18" rx="6" transform="rotate(-30 20 37)"/></svg></div><div class="tool-label">Backlink Maker</div></div>
    <div class="tool"><div class="tool-icon"><svg viewBox="0 0 48 48"><text x="3" y="15" class="f" font-family="Roboto,sans-serif" font-size="12" font-weight="700">1</text><text x="3" y="30" class="f" font-family="Roboto,sans-serif" font-size="12" font-weight="700">2</text><text x="3" y="45" class="f" font-family="Roboto,sans-serif" font-size="12" font-weight="700">3</text><path class="f" d="M14 8h32v5H14zM14 23h32v5H14zM14 38h32v5H14z"/></svg></div><div class="tool-label">Website Link Count Checker</div></div>
    <div class="tool"><div class="tool-icon"><svg viewBox="0 0 48 48" style="stroke-width:4.5"><path d="M20 12l4-4a8 8 0 0112 12l-4 4M28 36l-4 4A8 8 0 0112 28l4-4M8 16l-4-2M14 8l-2-4M40 32l4 2M34 40l2 4"/></svg></div><div class="tool-label">Website Broken Link Checker</div></div>
    <div class="tool"><div class="tool-icon"><svg viewBox="0 0 48 48" style="width:70px"><rect class="f" x="2" y="10" width="44" height="28"/><rect x="7" y="15" width="34" height="18" stroke="#fff" stroke-width="2"/><circle cx="24" cy="24" r="6" fill="#fff" stroke="none"/><text x="21.5" y="28" class="f" font-family="Roboto,sans-serif" font-size="10" font-weight="700">1</text></svg></div><div class="tool-label">Link Price Calculator</div></div>
    <div class="tool"><div class="tool-icon"><svg viewBox="0 0 48 48" style="stroke-width:4.5"><path d="M38 20a15 15 0 00-27-6M10 28a15 15 0 0027 6"/><path class="f" d="M6 6v12h12zM42 42V30H30z"/></svg></div><div class="tool-label">Reciprocal Link Checker</div></div>
    <div class="tool"><div class="tool-icon"><svg viewBox="0 0 48 48"><path d="M4 10l13-5 14 5 13-5v33l-13 5-14-5-13 5zM17 5v33M31 10v33"/></svg></div><div class="tool-label">Website Link Analyzer Tool</div></div>
  </div>
</section>

<a class="view-more">VIEW MORE</a>

<aside class="sidebar">
  <div class="ad ad-plag">
    <span class="tag">Try now Free</span>
    <span class="kicker">Premium</span>
    <span class="title">Plagiarism<br>Checker</span>
    <span class="sub">with Unlimited Searches</span>
    <span class="corner">Check<br>Now</span>
  </div>
  <div class="ad ad-da70" role="img" aria-label="Backlink offer banner with a hummingbird photo">
    <span class="big">DA70+</span>
    <span class="mid">Backlinks</span>
    <span class="pill">$5/Month</span>
  </div>
  <div class="popular">
    <div class="popular-head">Popular SEO Tools</div>
    <ol class="popular-list">
      <li>1. Plagiarism Checker</li>
      <li>2. Article Spinner / Rewriter</li>
      <li class="active">3. Keyword Position Checker</li>
      <li>4. Grammar Checker</li>
      <li>5. Domain Authority Checker</li>
      <li>6. Seekly PR Checker</li>
      <li>7. Image Compression Tool</li>
      <li>8. Reverse Image Search</li>
      <li>9. Page Authority checker</li>
      <li>10. Spell Checker</li>
      <li>11. Backlink Checker</li>
      <li>12. Rankora Rank Checker</li>
      <li>13. Backlink Maker</li>
      <li>14. Domain Age Checker</li>
      <li>15. Website Ping Tool</li>
      <li>16. Website Seo Score Checker</li>
      <li>17. Keyword Density Checker</li>
      <li>18. Website Page Size Checker</li>
      <li>19. Seekly Cache Checker</li>
      <li>20. Linkrank Checker</li>
    </ol>
  </div>
  <div class="rank-box">
    <div class="line1">Check all your site's rankings</div>
    <div class="line2">in 640+ search engines <span style="color:#e02a2a">free!</span></div>
    <div class="rank-bar"><div class="rank-input">www.your</div><div class="rank-btn">Check</div></div>
  </div>
  <div class="ad ad-da80">
    <span class="big">DA 80</span>
    <span class="bar"></span>
    <span class="buy">Buy Links <span>from</span> $0.24</span>
  </div>
  <div class="ad ad-boost">
    <div class="person" role="img" aria-label="Photo of a smiling man giving a thumbs up"></div>
    <span class="h1">BOOST YOUR RANKING</span>
    <span class="h2">ON SEEKLY</span>
    <span class="h3">WITHIN 3 WEEKS</span>
    <span class="side">100'S<br>OF<br>POSITIVE<br>REVIEWS</span>
    <span class="price">Only<b>$15.00</b></span>
  </div>
</aside>

<footer class="site-footer">
  <div class="footer-about">
    <div class="footer-head">About Us</div>
    <p>Bright Page Kit is one of the biggest free SEO tools provider. All tools are of premium quality and totally free.<br>Copyright © 2012-2017 by Brightpagekit.com. All Rights Reserved.</p>
  </div>
  <div class="footer-links">
    <div class="footer-head">Useful Links</div>
    <div class="links">Terms of Services<span>|</span>Testimonials<span>|</span>Privacy<span>|</span>Contact Us</div>
    <div class="subscribe-label">Subscribe for Newsletters:</div>
    <div class="subscribe">
      <div class="subscribe-ico"><svg width="14" height="10" viewBox="0 0 14 10"><rect width="14" height="10" fill="#fff"/><path d="M0 0l7 5 7-5" stroke="#137a47" fill="none" stroke-width="1.4"/></svg></div>
      <div class="subscribe-input">Enter your Email Address</div>
      <div class="subscribe-btn">Subscribe Now</div>
    </div>
  </div>
</footer>

</body>
</html>
```